Informational Website for SOLVANE-SOciety of Linked VAriable NEtwork Health Analysts

I need an informational website to help establish us as a legitimate entity. This will help us as we seek funding in to perform the research we intend to carry out. We are a newly formed group of family physicians and primary care researchers from 9 different countries around the world. We have access to electronic medical record data and/or health insurance claims data in our respective countries. We intend to perform international comparative studies in primary care. Our set of projects are to study the impact of the COVID-19 pandemic on primary care in our respective countries and around the world.
I've already purchased a domain and website from Plonko. It is a premium account. The domain is https://www.solvanehealthnet.org

Target Market(s)

Researchers, policy makers, universities, research funding agencies

Coding

Coded - Design and coding required

Number of Pages Required

5+ page

Font styles to use
Sans Serif

Requirements
Must have
• Must have our logo and an interactive map of the world highlighting Canada, Australia, China (including Hong Kong), Norway, Singapore, South Korea, Sweden, United Kingdom, United States.
This map must be editable such that we can add or remove countries and cities as we evolve. Please see attached brief.
Nice to have
• Nice to depict primary care and big data research

```html
<!DOCTYPE html>
<html lang="en">
<head>
<meta charset="utf-8">
<title>SOLVANE – Society of Linked Variable Network Health Analysts</title>
<link rel="stylesheet" href="https://fonts.googleapis.com/css2?family=Montserrat:wght@400;500;600;700&family=Open+Sans:wght@400;600&display=swap">
<style>
:root{
  --navy:#1d3f8c;
  --navy-dark:#152f6b;
  --green:#86b51c;
  --green-dark:#6f9a12;
  --ink:#2b2b2b;
  --muted:#6d6d6d;
  --light:#f1f2f3;
  --white:#ffffff;
}
*{box-sizing:border-box;margin:0;padding:0}
html,body{width:1200px;height:4264px;overflow:hidden}
body{font-family:"Open Sans",Arial,sans-serif;color:var(--ink);background:var(--white);position:relative}
h1,h2,h3,.nav,.btn{font-family:"Montserrat",Arial,sans-serif}

/* header */
.site-header{position:absolute;top:0;left:0;width:1200px;height:88px;display:flex;align-items:center;justify-content:space-between;padding:0 40px;background:var(--white)}
.brand{display:flex;align-items:center;gap:10px;font-family:"Montserrat",sans-serif;font-weight:700;font-size:30px;color:var(--navy)}
.brand-dot{width:34px;height:34px;border-radius:50%;background:var(--green)}
.nav{display:flex;gap:26px;font-size:13px;font-weight:500;color:#555}
.nav a{color:inherit;text-decoration:none;padding-bottom:4px}
.nav a.active{color:var(--navy);font-weight:700;border-bottom:2px solid var(--navy)}

/* hero */
.hero{position:absolute;top:88px;left:0;width:1200px;height:520px;background:linear-gradient(120deg,#0e2236 0%,#1f4a63 45%,#122b3e 100%);text-align:center;color:var(--white)}
.hero h1{margin-top:140px;font-size:70px;font-weight:700;letter-spacing:1px;line-height:1}
.hero p{margin:14px auto 0;width:760px;font-family:"Montserrat",sans-serif;font-size:36px;font-weight:500;line-height:1.2}
.btn{display:inline-block;font-size:13px;font-weight:600;letter-spacing:1px;text-transform:uppercase;padding:10px 26px;border:2px solid var(--white);color:var(--white);text-decoration:none}
.hero .btn{margin-top:26px;background:var(--white);color:var(--navy)}

/* feature cards */
.feature{position:absolute;top:588px;width:300px;height:250px;background:var(--white);box-shadow:0 6px 18px rgba(0,0,0,.15);text-align:center;padding:36px 28px 0}
.feature.pub{left:138px}
.feature.pres{left:450px;top:560px;height:300px;border:3px solid var(--green);padding-top:36px}
.feature.grant{left:762px}
.feature h3{font-size:22px;font-weight:700;color:var(--navy);margin-top:14px}
.feature.pres h3{color:var(--green)}
.feature p{font-size:14px;color:var(--muted);line-height:1.45;margin-top:8px}

/* about */
.about{position:absolute;top:960px;left:0;width:1200px;height:520px;background:linear-gradient(135deg,#1b3f8f,#234da3 60%,#1a3b85)}
.about-art{position:absolute;left:170px;top:90px;width:360px;height:340px;border-radius:50%;background:radial-gradient(circle,rgba(255,255,255,.25),rgba(255,255,255,.06))}
.about-copy{position:absolute;left:590px;top:100px;width:530px;color:var(--white)}
.about-copy h2{font-size:42px;font-weight:500;border-top:2px solid var(--white);display:inline-block;padding-top:6px}
.about-copy p{margin-top:20px;font-size:15px;line-height:1.75;color:#dfe6f5}
.about-copy .btn{margin-top:30px}

/* what we do */
.section-title{position:absolute;left:0;width:1200px;text-align:center;font-family:"Montserrat",sans-serif;font-size:40px;font-weight:500;color:var(--navy)}
.section-title b{color:var(--green);font-weight:500}
.title-rule{position:absolute;left:560px;width:80px;height:3px;background:var(--navy)}
.service{position:absolute;top:1735px;width:310px;height:310px;border-radius:50%;border:3px solid var(--navy);background:var(--white);text-align:center;padding-top:120px}
.service.primary{left:108px}
.service.family{left:445px;top:1700px;width:320px;height:320px;border:none;background:var(--green);color:var(--white);padding-top:130px}
.service.data{left:770px}
.service h3{font-size:22px;font-weight:500;color:var(--navy)}
.service.family h3{color:var(--white)}
.service p{font-size:13px;color:var(--muted);line-height:1.5;width:190px;margin:10px auto 0}
.service.family p{color:#eef5dc}
.badge{position:absolute;left:50%;transform:translateX(-50%);width:104px;height:104px;border-radius:50%;background:var(--green);border:6px solid var(--white);box-shadow:0 0 0 2px var(--navy);display:flex;align-items:center;justify-content:center}
.service .badge{top:-32px}
.service.family .badge{background:var(--navy);box-shadow:0 0 0 2px var(--white);top:-40px}

/* institutions */
.institutions{position:absolute;top:2100px;left:0;width:1200px;height:420px;background:var(--light)}
.institutions h2{margin-top:82px;text-align:center;font-size:34px;font-weight:700;color:#222}
.institutions h2 span{font-weight:400}
.partners{position:absolute;top:222px;left:110px;width:980px;display:flex;justify-content:space-around;align-items:center}
.partner{font-family:"Montserrat",sans-serif;font-size:24px;font-weight:500;color:var(--navy);display:flex;align-items:center;gap:10px}
.partner .sq{width:22px;height:22px;background:var(--green)}
.arrow{position:absolute;top:228px;font-size:38px;color:#666;font-family:"Montserrat",sans-serif}

/* map */
.map{position:absolute;top:2680px;left:60px;width:1080px;height:560px;background:linear-gradient(180deg,#e9eaec,#dcdde0);border-radius:6px}
.pin{position:absolute;width:22px;height:30px}

/* contact */
.contact{position:absolute;top:3280px;left:0;width:1200px;height:680px;background:var(--green)}
.contact-photo{position:absolute;left:110px;top:170px;width:360px;height:360px;border-radius:50%;background:radial-gradient(circle at 40% 40%,#5d84b9,#1b3560 75%);border:10px solid rgba(255,255,255,.35)}
.contact-form{position:absolute;left:670px;top:160px;width:450px}
.contact-form h2{font-size:40px;font-weight:700;color:var(--white);margin-bottom:20px}
.contact-form h2 span{font-weight:400}
.field{height:42px;background:var(--white);border-radius:22px;margin-bottom:14px;padding:0 20px;display:flex;align-items:center;justify-content:space-between;font-size:13px;color:#888}
.field.message{height:110px;border-radius:16px;align-items:flex-start;padding-top:12px}
.submit{height:44px;border-radius:22px;background:var(--navy);color:var(--white);font-family:"Montserrat",sans-serif;font-weight:700;font-size:14px;letter-spacing:1px;display:flex;align-items:center;justify-content:center;margin-top:6px}

/* footer */
.site-footer{position:absolute;top:3960px;left:0;width:1200px;height:304px;background:var(--white);text-align:center}
.site-footer .brand{justify-content:center;margin-top:50px;font-size:40px}
.site-footer .brand-dot{width:46px;height:46px}
.footer-nav{margin-top:36px;display:flex;justify-content:center;gap:28px;font-family:"Montserrat",sans-serif;font-size:13px;color:#444}
.copyright{margin-top:16px;font-size:12px;color:#666}
.social{margin-top:14px;display:flex;justify-content:center;gap:10px}
.social span{width:28px;height:28px;border-radius:50%;background:var(--navy)}
</style>
</head>
<body>

<header class="site-header">
  <div class="brand"><span class="brand-dot"></span>SOLVANE</div>
  <nav class="nav">
    <a class="active" href="#">HOME</a><a href="#">ABOUT US</a><a href="#">PARTICIPATING INSTITUTIONS</a><a href="#">PUBLICATION</a><a href="#">PRESENTATION</a><a href="#">GRANTS</a><a href="#">NEWS</a>
  </nav>
</header>

<section class="hero" role="img" aria-label="Researchers working with data screens in a dim office">
  <h1>SOLVANE</h1>
  <p>SOciety of Linked VAriable NEtwork Health Analysts</p>
  <a class="btn" href="#">Read more</a>
</section>

<article class="feature pub">
  <svg width="60" height="48" viewBox="0 0 60 48"><rect x="4" y="6" width="52" height="36" rx="4" fill="none" stroke="#1d3f8c" stroke-width="4"/><line x1="14" y1="18" x2="46" y2="18" stroke="#1d3f8c" stroke-width="4"/><line x1="14" y1="28" x2="40" y2="28" stroke="#1d3f8c" stroke-width="4"/></svg>
  <h3>PUBLICATIONS</h3>
  <p>Lorem ipsum dolor sit amet, consectetur adipiscing elit, sed do eiusmod tempor</p>
</article>
<article class="feature pres">
  <svg width="60" height="52" viewBox="0 0 60 52"><rect x="6" y="4" width="48" height="30" fill="none" stroke="#86b51c" stroke-width="4"/><line x1="30" y1="34" x2="30" y2="48" stroke="#86b51c" stroke-width="4"/><line x1="18" y1="48" x2="42" y2="48" stroke="#86b51c" stroke-width="4"/></svg>
  <h3>PRESENTATION</h3>
  <p>Lorem ipsum dolor sit amet, consectetur adipiscing elit, sed do eiusmod tempor incididunt ut labore et dolore</p>
</article>
<article class="feature grant">
  <svg width="48" height="54" viewBox="0 0 48 54"><rect x="6" y="4" width="36" height="46" rx="3" fill="none" stroke="#1d3f8c" stroke-width="4"/><circle cx="24" cy="20" r="7" fill="none" stroke="#1d3f8c" stroke-width="4"/><line x1="14" y1="38" x2="34" y2="38" stroke="#1d3f8c" stroke-width="4"/></svg>
  <h3>GRANTS</h3>
  <p>Lorem ipsum dolor sit amet, consectetur adipiscing elit, sed do eiusmod tempor</p>
</article>

<section class="about">
  <div class="about-art" role="img" aria-label="Decorative globe and stethoscope graphic"></div>
  <div class="about-copy">
    <h2>ABOUT SOLVANE</h2>
    <p>We are family physicians and primary care researchers from 9 different countries around the world. We have access to electronic medical record data and/or health insurance claims data in our respective countries. We intend to perform international comparative studies in primary care. Our first project is to study the impact of the COVID-19 pandemic on primary care in our countries.</p>
    <a class="btn" href="#">Read more</a>
  </div>
</section>

<h2 class="section-title" style="top:1555px">WHAT <b>WE DO</b></h2>
<div class="title-rule" style="top:1612px"></div>

<div class="service primary">
  <div class="badge"><svg width="44" height="44" viewBox="0 0 44 44"><path d="M16 4h12v12h12v12H28v12H16V28H4V16h12z" fill="none" stroke="#fff" stroke-width="3"/></svg></div>
  <h3>PRIMARY CARE</h3>
  <p>Lorem ipsum dolor sit amet, consectetur adipiscing elit, sed do eiusmod tempor</p>
</div>
<div class="service family">
  <div class="badge"><svg width="44" height="44" viewBox="0 0 44 44"><rect x="8" y="4" width="28" height="36" rx="3" fill="none" stroke="#fff" stroke-width="3"/><path d="M22 14v12M16 20h12" stroke="#fff" stroke-width="3"/></svg></div>
  <h3>FAMILY MEDICINE</h3>
  <p>Lorem ipsum dolor sit amet, consectetur adipiscing elit, sed do eiusmod tempor</p>
</div>
<div class="service data">
  <div class="badge"><svg width="44" height="44" viewBox="0 0 44 44"><rect x="6" y="6" width="32" height="26" fill="none" stroke="#fff" stroke-width="3"/><path d="M12 26l7-8 6 5 8-10" fill="none" stroke="#fff" stroke-width="3"/><line x1="14" y1="38" x2="30" y2="38" stroke="#fff" stroke-width="3"/></svg></div>
  <h3>DATA RESEARCH</h3>
  <p>Lorem ipsum dolor sit amet, consectetur adipiscing elit, sed do eiusmod tempor</p>
</div>

<section class="institutions">
  <h2>PARTICIPATING <span>INSTITUTIONS</span></h2>
  <div class="title-rule" style="top:140px"></div>
  <span class="arrow" style="left:16px">&lsaquo;</span>
  <div class="partners">
    <div class="partner"><span class="sq"></span>Kestrel Health</div>
    <div class="partner"><span class="sq"></span>Ambrose Centre</div>
    <div class="partner"><span class="sq"></span>Linmoor Council</div>
    <div class="partner"><span class="sq"></span>Farrow College</div>
  </div>
  <span class="arrow" style="right:16px">&rsaquo;</span>
</section>

<h2 class="section-title" style="top:2565px">OUR LOCATION</h2>
<div class="title-rule" style="top:2622px"></div>
<div class="map" role="img" aria-label="World map highlighting member countries">
  <svg class="pin" style="left:165px;top:170px" viewBox="0 0 22 30"><path d="M11 0a11 11 0 0 1 11 11c0 8-11 19-11 19S0 19 0 11A11 11 0 0 1 11 0z" fill="#1d3f8c"/><circle cx="11" cy="11" r="4" fill="#fff"/></svg>
  <svg class="pin" style="left:245px;top:220px" viewBox="0 0 22 30"><path d="M11 0a11 11 0 0 1 11 11c0 8-11 19-11 19S0 19 0 11A11 11 0 0 1 11 0z" fill="#1d3f8c"/><circle cx="11" cy="11" r="4" fill="#fff"/></svg>
  <svg class="pin" style="left:500px;top:165px" viewBox="0 0 22 30"><path d="M11 0a11 11 0 0 1 11 11c0 8-11 19-11 19S0 19 0 11A11 11 0 0 1 11 0z" fill="#1d3f8c"/><circle cx="11" cy="11" r="4" fill="#fff"/></svg>
  <svg class="pin" style="left:530px;top:135px" viewBox="0 0 22 30"><path d="M11 0a11 11 0 0 1 11 11c0 8-11 19-11 19S0 19 0 11A11 11 0 0 1 11 0z" fill="#1d3f8c"/><circle cx="11" cy="11" r="4" fill="#fff"/></svg>
  <svg class="pin" style="left:560px;top:130px" viewBox="0 0 22 30"><path d="M11 0a11 11 0 0 1 11 11c0 8-11 19-11 19S0 19 0 11A11 11 0 0 1 11 0z" fill="#1d3f8c"/><circle cx="11" cy="11" r="4" fill="#fff"/></svg>
  <svg class="pin" style="left:880px;top:205px" viewBox="0 0 22 30"><path d="M11 0a11 11 0 0 1 11 11c0 8-11 19-11 19S0 19 0 11A11 11 0 0 1 11 0z" fill="#1d3f8c"/><circle cx="11" cy="11" r="4" fill="#fff"/></svg>
  <svg class="pin" style="left:860px;top:255px" viewBox="0 0 22 30"><path d="M11 0a11 11 0 0 1 11 11c0 8-11 19-11 19S0 19 0 11A11 11 0 0 1 11 0z" fill="#1d3f8c"/><circle cx="11" cy="11" r="4" fill="#fff"/></svg>
  <svg class="pin" style="left:830px;top:330px" viewBox="0 0 22 30"><path d="M11 0a11 11 0 0 1 11 11c0 8-11 19-11 19S0 19 0 11A11 11 0 0 1 11 0z" fill="#1d3f8c"/><circle cx="11" cy="11" r="4" fill="#fff"/></svg>
  <svg class="pin" style="left:935px;top:460px" viewBox="0 0 22 30"><path d="M11 0a11 11 0 0 1 11 11c0 8-11 19-11 19S0 19 0 11A11 11 0 0 1 11 0z" fill="#1d3f8c"/><circle cx="11" cy="11" r="4" fill="#fff"/></svg>
</div>

<section class="contact">
  <div class="contact-photo" role="img" aria-label="Researcher interacting with a holographic data display"></div>
  <div class="contact-form">
    <h2>CONTACT <span>US</span></h2>
    <div class="field">Full Name*</div>
    <div class="field">Email*</div>
    <div class="field">Phone No.</div>
    <div class="field">Are you a Researcher?<svg width="12" height="8" viewBox="0 0 12 8"><path d="M1 1l5 5 5-5" fill="none" stroke="#888" stroke-width="2"/></svg></div>
    <div class="field message">Message</div>
    <div class="submit">SUBMIT NOW</div>
  </div>
</section>

<footer class="site-footer">
  <div class="brand"><span class="brand-dot"></span>SOLVANE</div>
  <div class="footer-nav"><span>HOME</span><span>ABOUT US</span><span>PARTICIPATING INSTITUTION</span><span>PUBLICATION</span><span>PRESENTATION</span><span>GRANTS</span><span>NEWS</span></div>
  <p class="copyright">© 2021 SOLVANE. All Rights Reserved.</p>
  <div class="social"><span></span><span></span><span></span><span></span></div>
</footer>

</body>
</html>
```